Harwick DCS Informational Flyer

We need a visually-appealing informational 1-page (Letter paper, 8.5 by 11.0 inches, portrait orientation) handout to promote academic and research programs of Harwick University Department of Digital and Computing Studies. This handout will be sent to other universities to recruit students and used and job/career fairs to promote the computing programs at Harwick.

Target Market(s)

Prospective graduate students in computing (both in US and international)

Industry/Entity Type

Education

Requirements
Must have
• (1) Incorporate (most of) the department information in a visually appealing way
• (2) Follow Harwick Brand Guidelines: https://identity.harwickuni.edu/brand-guidelines
Nice to have
• Background pictures of Philadelphia, Harwick University, and/or NAVL building (http://sdp.harwickuni.edu/research/NAVL)

```html
<!DOCTYPE html>
<html lang="en">
<head>
<meta charset="utf-8">
<title>Harwick DCS Informational Flyer</title>
<link rel="stylesheet" href="https://fonts.googleapis.com/css2?family=Libre+Baskerville&family=Arimo&display=swap">
<style>
  :root {
    --page-bg: #f1f1f2;
    --sheet: #ffffff;
    --sheet-edge: #dcdcdf;
    --maroon: #9d1c36;
    --maroon-deep: #7a1228;
    --maroon-light: #b8324d;
    --ink: #1b1b1b;
    --panel-top: #454545;
    --panel-bottom: #0e0e0e;
    --panel-text: #f2f2f2;
  }
  * { box-sizing: border-box; margin: 0; padding: 0; }
  html, body { width: 938px; height: 1200px; overflow: hidden; }
  body { background: var(--page-bg); font-family: "Arimo", Arial, sans-serif; position: relative; }

  .sheet {
    position: absolute; left: 36px; top: 42px; width: 868px; height: 1122px;
    background: linear-gradient(160deg, #ffffff 0%, #f6f6f7 50%, #ffffff 100%);
    border: 2px solid var(--sheet-edge);
  }

  .brand { position: absolute; left: 103px; top: 99px; display: flex; align-items: center; gap: 12px; }
  .brand-square { width: 62px; height: 64px; background: var(--maroon); }
  .brand-name {
    font-family: "Libre Baskerville", Georgia, serif; color: var(--maroon);
    font-size: 27px; line-height: 30px; letter-spacing: 1px; text-transform: uppercase;
  }

  .about { position: absolute; left: 100px; top: 208px; width: 349px; }
  .about h1 {
    font-family: "Libre Baskerville", Georgia, serif; font-weight: 400;
    color: var(--maroon); font-size: 23px; line-height: 30px; margin-bottom: 3px;
  }
  .about p {
    font-size: 16.3px; line-height: 24.3px; color: var(--ink);
    text-align: justify; letter-spacing: -0.1px;
  }

  .photo-band {
    position: absolute; left: 38px; top: 584px; width: 864px; height: 478px;
    background: linear-gradient(180deg, var(--maroon) 0%, var(--maroon-light) 45%, var(--maroon-deep) 100%);
  }

  .facts {
    position: absolute; left: 499px; top: 86px; width: 360px; height: 542px;
    background: linear-gradient(180deg, var(--panel-top) 0%, #2a2a2a 45%, var(--panel-bottom) 100%);
    color: var(--panel-text); font-size: 11.6px; line-height: 13.7px;
    padding: 22px 12px 0 7px;
  }
  .facts-pointer { position: absolute; left: 775px; top: 627px; }
  .facts section { margin-bottom: 9px; }
  .facts h2 { font-weight: 400; font-size: 11.6px; text-transform: uppercase; }
  .facts h2::before { content: "\25CF  "; }
  .facts h2 small { font-size: 9px; text-transform: none; }
  .facts ul { list-style: none; }
  .facts li { padding-left: 11px; text-indent: -11px; }
  .facts .open li::before { content: "\25CB  "; }
  .facts .dot li::before { content: "\2022  "; }
  .facts sup { font-size: 6px; vertical-align: 1px; }
  .facts .research-lead { margin-top: 12px; }

  .contact {
    position: absolute; left: 0; top: 1101px; width: 938px; text-align: center;
    font-size: 13px; color: var(--maroon);
  }
  .contact .web { color: var(--ink); }
</style>
</head>
<body>
  <div class="sheet"></div>

  <div class="brand">
    <div class="brand-square"></div>
    <div class="brand-name">Harwick<br>University</div>
  </div>

  <article class="about">
    <h1>About Harwick University</h1>
    <p>Harwick University is an R1 (highest research activity) institution that ranks among the top 55 among public colleges and universities in the National College Review ranking. Serving more than 38,000 students, Harwick is the 26th largest university and 6th largest provider of graduate school education in the United States. Located in the heart of Philadelphia, Harwick offers students opportunities to explore the 5th largest city in U.S., known for its arts, culture and history, and affordable living. In addition, Harwick University is in close proximity to many companies specializing in information technology, health care, biotechnology, and finance.</p>
  </article>

  <div class="photo-band" role="img" aria-label="Group of smiling students giving thumbs up, tinted in maroon"></div>

  <aside class="facts">
    <section>
      <h2>People</h2>
      <ul class="open">
        <li>60 faculty members</li>
        <li>1000 undergraduate students</li>
        <li>100 graduate students</li>
        <li>Harwick DCS alums work at companies such as Brightcart, Friendloop, Voltmark, Searchwell, Corebyte Systems, Hollis Grant Bank, Careerlink, Softvane, Datacrest</li>
      </ul>
    </section>
    <section>
      <h2>Degree Programs</h2>
      <ul class="open">
        <li>B.A. and B.S. in Computer Science (CS)</li>
        <li>B.A. and B.S. in Information Science &amp; Technology (IS&amp;T)</li>
        <li>PSM in Cyber Defense and Information Assurance</li>
        <li>M.S. in Computer Science</li>
        <li>M.S. in Computational Data Science</li>
        <li>M.S. in Information Science and Technology</li>
        <li>Ph.D. in Computer and Information Sciences</li>
      </ul>
    </section>
    <section>
      <h2>Department Rankings <small>(according to http://compdeptrank.org)</small></h2>
      <ul class="open">
        <li>70<sup>th</sup> overall in US CS departments</li>
        <li>16<sup>th</sup> in computer networks</li>
        <li>22<sup>nd</sup> in computer vision</li>
        <li>34<sup>th</sup> in artificial intelligence</li>
        <li>35<sup>th</sup> in operating systems</li>
      </ul>
    </section>
    <section>
      <h2>Research</h2>
      <ul class="open">
        <li>Over $3 million in annual external research funding from sources such as NRF, NHRA, Aerospace Command, ARPO, DSA, the State of Eastland, and industry</li>
      </ul>
      <ul class="open research-lead">
        <li>Research focus areas:</li>
      </ul>
      <ul class="dot">
        <li>Artificial Intelligence</li>
        <li>Computer Vision</li>
        <li>Data Mining and Machine Learning</li>
        <li>Information Security and Forensics</li>
        <li>Operating and Distributed Systems</li>
        <li>Web Data Management</li>
        <li>Wireless Networks and Mobile Computing</li>
      </ul>
    </section>
  </aside>
  <svg class="facts-pointer" width="57" height="26" viewBox="0 0 57 26" aria-hidden="true">
    <polygon points="0,0 57,0 28.5,25" fill="#0e0e0e"/>
  </svg>

  <footer class="contact">
    Contact Info :&nbsp; (215) 555-0148 &bull; dcsadmissions@harwickuni.edu &nbsp;&bull;&nbsp; <span class="web">http://dcs.harwickuni.edu &bull; http://dcs.harwickuni.edu/GradAdmissions</span>
  </footer>
</body>
</html>
```